Business Card for Auto Dealership - Clean, sharp and professional

Please use the maroon logo with the grey background. Need a sharp, clean and professional business card for an Auto Dealer. In the files provides there is three different logos. I have not decided which one to go with yet. Right now I am favoring the grey/silver background. I would like my contact info on there and the website as well. I feel like less is more and want something simple, clean and sharp. Thank you in advance for your tie and effort! I also need email signature, letterhead, etc after this

Target Market(s)

Car buyers

Industry/Entity Type

Automotive

Contact Information for Business Card

Drew
555-214-7730
www.BriarvaleAutoLink.example
Drew@BriarvaleAutoLink.example

Font styles to use
Serif
Sans Serif

Requirements
Must have
• Please use the maroon logo with the grey background. Business Card Details and logo from files. Please stick to the logo colors

```html
<!DOCTYPE html>
<html lang="en">
<head>
<meta charset="utf-8">
<title>Briarvale Auto Link – Business Cards</title>
<link rel="stylesheet" href="https://fonts.googleapis.com/css2?family=Arimo:wght@400;700&display=swap">
<style>
  :root {
    --board-top: #1a6fb3;
    --board-bottom: #0b5391;
    --maroon: #4a1816;
    --card-grey: #e8e9eb;
    --card-ice: #e9f0f8;
    --panel-grey: #e6e6e6;
    --fold-dark: #9a9a9a;
    --fold-light: #bdbdbd;
    --ink: #3f3f3f;
    --ink-soft: #7a7a7a;
    --mark-grey: #8a8a8a;
    --white: #ffffff;
  }
  * { margin: 0; padding: 0; box-sizing: border-box; }
  html, body { width: 1200px; height: 943px; overflow: hidden; }
  body {
    position: relative;
    background: linear-gradient(135deg, var(--board-top), var(--board-bottom));
    font-family: "Arimo", Arial, sans-serif;
  }
  .side-label {
    position: absolute; left: 333px; top: 133px;
    color: var(--white); font-weight: 700; font-size: 24px;
  }
  .card {
    position: absolute; width: 447px; height: 254px; overflow: hidden;
    box-shadow: 0 14px 22px rgba(0, 20, 50, 0.35);
  }
  .card--back { left: 138px; top: 170px; background: var(--card-grey); }
  .card--grey-front { left: 615px; top: 170px; background: var(--card-grey); }
  .card--maroon-front { left: 138px; top: 518px; background: var(--white); }
  .card--ice-front { left: 615px; top: 518px; background: var(--card-ice); }

  .brand { position: absolute; display: flex; align-items: center; gap: 10px; }
  .brand__dot { border-radius: 50%; flex: none; }
  .brand__name { font-weight: 700; letter-spacing: 0.5px; line-height: 1.1; white-space: nowrap; }
  .brand__name span { display: block; }

  .card--back .brand { left: 118px; top: 97px; }
  .card--back .brand__dot { width: 60px; height: 60px; background: var(--maroon); }
  .card--back .brand__name { color: var(--maroon); font-size: 19px; }

  .card--grey-front .brand { left: 261px; top: 42px; }
  .card--grey-front .brand__dot { width: 42px; height: 42px; background: var(--mark-grey); }
  .card--grey-front .brand__name { color: var(--mark-grey); font-size: 14px; }

  .card--ice-front .brand { left: 33px; top: 33px; }
  .card--ice-front .brand__dot { width: 42px; height: 42px; background: var(--ink); }
  .card--ice-front .brand__name { color: var(--ink); font-size: 14px; }

  .holder { position: absolute; color: var(--ink); font-weight: 700; font-size: 31px; line-height: 1; }
  .contact { position: absolute; list-style: none; color: var(--ink-soft); font-size: 13px; line-height: 23px; }

  .card--grey-front .holder { left: 46px; top: 52px; }
  .card--grey-front .contact { left: 46px; top: 146px; }

  .card--ice-front .holder { right: 270px; top: 133px; }
  .card--ice-front .divider { position: absolute; left: 199px; top: 97px; width: 2px; height: 104px; background: var(--ink); }
  .card--ice-front .contact { left: 217px; top: 124px; color: var(--ink); font-size: 12.5px; line-height: 21px; }

  .card--maroon-front svg { display: block; }
</style>
</head>
<body>
  <div class="side-label">BACK</div>

  <section class="card card--back">
    <div class="brand">
      <span class="brand__dot"></span>
      <span class="brand__name"><span>BRIARVALE</span><span>AUTO LINK</span></span>
    </div>
  </section>

  <section class="card card--grey-front">
    <div class="holder">DREW</div>
    <div class="brand">
      <span class="brand__dot"></span>
      <span class="brand__name"><span>BRIARVALE</span><span>AUTO LINK</span></span>
    </div>
    <ul class="contact">
      <li>555-214-7730</li>
      <li>www.BriarvaleAutoLink.example</li>
      <li>Drew@BriarvaleAutoLink.example</li>
    </ul>
  </section>

  <section class="card card--maroon-front">
    <svg width="447" height="254" viewBox="0 0 378 215" font-family="Arimo, Arial, sans-serif">
      <polygon class="band" points="0,0 238,0 170,215 0,215" fill="var(--maroon)"/>
      <polygon class="fold-top" points="181,29 238,0 218,29" fill="var(--fold-dark)"/>
      <polygon class="fold-bottom" points="153,189 170,215 190,189" fill="var(--fold-light)"/>
      <polygon class="panel" points="181,29 355,29 355,189 153,189" fill="var(--panel-grey)"/>
      <circle class="brand-dot" cx="46" cy="100" r="17" fill="var(--white)"/>
      <text class="brand-name" fill="var(--white)" font-weight="700" font-size="11" letter-spacing="0.4">
        <tspan x="70" y="98">BRIARVALE</tspan>
        <tspan x="70" y="110">AUTO LINK</tspan>
      </text>
      <text x="336" y="70" text-anchor="end" fill="var(--ink)" font-weight="700" font-size="24">DREW</text>
      <g fill="var(--ink-soft)" font-size="9.5" text-anchor="end">
        <text x="260" y="128">555-214-7730</text>
        <text x="330" y="146">www.BriarvaleAutoLink.example</text>
        <text x="330" y="164">Drew@BriarvaleAutoLink.example</text>
      </g>
    </svg>
  </section>

  <section class="card card--ice-front">
    <div class="brand">
      <span class="brand__dot"></span>
      <span class="brand__name"><span>BRIARVALE</span><span>AUTO LINK</span></span>
    </div>
    <div class="holder">DREW</div>
    <span class="divider"></span>
    <ul class="contact">
      <li>555-214-7730</li>
      <li>www.BriarvaleAutoLink.example</li>
      <li>Drew@BriarvaleAutoLink.example</li>
    </ul>
  </section>
</body>
</html>
```